5 facebook (and instagram) posts for advertising a service of Online Medicine.
This is NOT a facebook page design. This is just facebook (and Instagram) posts design.

We are a medical company providing medicine at distance, using standard videoconsultation and sometimes videoconsultation with a medical device that collects vital signs.

Each post should have:
- Our logo (attached) – if needed it can be just the circular form, but that´s up to you to decide. Ofcourse some design work can be done to this form (watermark, change in dimension, etc)
- Some posts can have the photo of the device (not all the posts because we also provide videoconsultations without the device) – for this please use our website to collect images (https://www.casaorvalhoverde.com/en/kordalix). You can also use the video of the device to collect images (provided as attachment).
- Some stock image at your decision or collected from our website (https://www.casaorvalhoverde.com/pt/medicina-online) or from the provided video (all of these are licensed and you can use them freely – for instance you can collect doctors from our video)
- One or more of the following headlines (please use different headlines for different posts):
 Revolução na Qualidade da Videoconsulta
 O seu Médico com acesso à informação da sua Orrin Wellbook
 Sincronização com Orrin Wellbook
 Possibilidade de usar o dispositivo Kordalix | Medição à Distância de 6 Sinais Vitais
 Revolução na Saúde
 Revolução na Medicina à Distância
 Um Novo Mundo na Saúde
 Segurança e Fiabilidade na Medicina à Distância
 Excelência na Medicina à Distância
 Baixa Médica Online
 Atestados de Saúde
 Renovação de Receituário
 Planos de Monitorização Remota e Acompanhamento Médico desde 10 EUR / Mês

We need 5 posts, all different between each other but where we can feel an aesthetical and graphic/design continuity/coherence of course.
Each post should be provided on adequate format for facebook and Instagram publishing.

Target Market(s)

Patients

Industry/Entity Type

Medicine

Requirements
Must have
• Check description
Nice to have
• Check description

```html
<!DOCTYPE html>
<html lang="pt">
<head>
<meta charset="utf-8">
<title>Casa Orvalho Verde – Revolução na Qualidade da Videoconsulta</title>
<link href="https://fonts.googleapis.com/css2?family=Oswald:wght@700&family=Roboto:wght@400;700;900&display=swap" rel="stylesheet">
<style>
  :root {
    --brand-blue: #1d9ccb;
    --deep-blue: #0a6e96;
    --accent-orange: #e8812b;
    --ink-grey: #5a5f66;
    --white: #ffffff;
    --bg-light: #f4f5f7;
    --bg-mid: #e6e8eb;
  }
  * { margin: 0; padding: 0; box-sizing: border-box; }
  html, body { width: 1200px; height: 1200px; overflow: hidden; }
  body { font-family: "Roboto", Arial, sans-serif; }

  .post {
    position: relative;
    width: 1200px;
    height: 1200px;
    overflow: hidden;
    background: linear-gradient(135deg, var(--bg-light) 0%, #ffffff 40%, var(--bg-mid) 70%, var(--bg-light) 100%);
  }

  .ring { position: absolute; inset: 0; }

  .brand {
    position: absolute;
    left: 398px;
    top: 48px;
    display: flex;
    align-items: center;
    gap: 18px;
  }
  .brand-dot {
    width: 84px; height: 84px;
    border-radius: 50%;
    background: var(--deep-blue);
    flex: none;
  }
  .brand-name {
    font-family: "Roboto", Arial, sans-serif;
    font-weight: 900;
    font-size: 40px;
    line-height: 38px;
    color: var(--brand-blue);
    letter-spacing: 0.5px;
    text-transform: uppercase;
  }
  .brand-tagline {
    font-size: 19px;
    line-height: 24px;
    color: var(--ink-grey);
    font-weight: 400;
    margin-top: 4px;
  }

  .message-panel {
    position: absolute;
    left: 109px;
    top: 220px;
    width: 500px;
    height: 586px;
    background: var(--brand-blue);
    border-top-right-radius: 180px;
  }
  .headline {
    position: absolute;
    left: 139px;
    top: 298px;
    font-family: "Oswald", Impact, sans-serif;
    font-weight: 700;
    font-size: 51px;
    line-height: 69px;
    color: var(--white);
    text-transform: uppercase;
  }
  .headline-rule {
    position: absolute;
    left: 139px;
    top: 513px;
    width: 331px;
    height: 3px;
    background: var(--white);
  }
  .lead {
    position: absolute;
    left: 139px;
    top: 538px;
    font-weight: 700;
    font-size: 26px;
    line-height: 40px;
    color: var(--white);
  }

  .photo {
    position: absolute;
    left: 542px;
    top: 303px;
    width: 548px;
    height: 718px;
    border-radius: 16px;
    background:
      radial-gradient(ellipse at 30% 45%, #9fc3d4 0%, rgba(159,195,212,0) 35%),
      radial-gradient(ellipse at 75% 70%, #e9ecef 0%, rgba(233,236,239,0) 45%),
      linear-gradient(160deg, #eef1f3 0%, #d9dde0 45%, #c7ccd0 75%, #e4e6e8 100%);
  }

  .web-bar {
    position: absolute;
    left: 342px;
    top: 1074px;
    width: 517px;
    height: 80px;
    border-radius: 8px;
    overflow: hidden;
    display: flex;
    background: var(--brand-blue);
  }
  .web-icon {
    width: 135px;
    height: 100%;
    background: var(--accent-orange);
    display: flex;
    align-items: center;
    justify-content: center;
  }
  .web-url {
    flex: 1;
    display: flex;
    align-items: center;
    padding-left: 21px;
    font-weight: 700;
    font-size: 22px;
    color: var(--white);
  }
</style>
</head>
<body>
  <main class="post">
    <svg class="ring" width="1200" height="1200" viewBox="0 0 1200 1200" aria-hidden="true">
      <circle cx="1218" cy="118" r="226" fill="none" stroke="var(--deep-blue)" stroke-width="52"/>
      <circle cx="-44" cy="1089" r="240" fill="none" stroke="var(--deep-blue)" stroke-width="56"/>
    </svg>

    <header class="brand">
      <span class="brand-dot"></span>
      <div>
        <div class="brand-name">Casa Orvalho<br>Verde</div>
        <div class="brand-tagline">Professor Doutor Tomás Varela</div>
      </div>
    </header>

    <section class="message-panel"></section>
    <h1 class="headline">Revolução na<br>qualidade da<br>videoconsulta</h1>
    <div class="headline-rule"></div>
    <p class="lead">Descubra como as nossas<br>videoconferências médicas<br>estão a transformar a forma<br>como você cuida da sua<br>saúde</p>

    <div class="photo" role="img" aria-label="Fotografia de um médico sorridente de barba grisalha, com auricular, a fazer uma videoconsulta com uma paciente visível no ecrã do computador"></div>

    <footer class="web-bar">
      <div class="web-icon">
        <svg width="52" height="52" viewBox="0 0 52 52" aria-hidden="true">
          <circle cx="26" cy="26" r="25" fill="var(--white)"/>
          <g fill="none" stroke="var(--accent-orange)" stroke-width="2.6">
            <circle cx="26" cy="26" r="14"/>
            <ellipse cx="26" cy="26" rx="6" ry="14"/>
            <line x1="12" y1="26" x2="40" y2="26"/>
            <path d="M14 19 H38 M14 33 H38"/>
          </g>
        </svg>
      </div>
      <div class="web-url">www.casaorvalhoverde.com</div>
    </footer>
  </main>
</body>
</html>
```